Print Ad for 2022 Prime Counsel Journal - Seeking a Creative Ad for a Creative Law Firm

We need an advertisement for the Prime Counsel annual publication, which will also be included in the Brookvale Gazette, a widely-read, stylish city magazine.

We would like our advertisement to be clever, stylish, and unique. We hate looking like other law firms and want an ad that is original, unexpected, clever, or stylish. We DO NOT want something traditional, boring, or typical for law firms - we separate ourselves in our market by NOT acting like a traditional law firm.

Marwick Tolland and Pryce, LLC provides full-service legal representation to entrepreneurs, individuals, and companies for all of their business, employment and litigation needs.
We have included THREE different photo options in the attachments. Please use ONLY ONE in the ad.

BE SURE TO REVIEW THE ATTACHMENTS. WE HAVE INCLUDED OUR ADS FOR PRIOR YEARS, BUT WE WANT A TOTALLY DIFFERENT LOOK THIS YEAR!! PLEASE DO NOT PROVIDE SIMILAR ADS.

For more information, please visit our website: www.mtplawgroup.example

Target Market(s)

Small business owners, individuals with employment law issues, entrepreneurs, other attorneys.

Industry/Entity Type

Legal

Font styles to use
Serif
Decorative

Colors

Designer to choose colors to be used in the design.

Requirements
Must have
• It must use our logo, our photo, and our tag line "The Name is Hard to Remember. The Results are Hard to Forget." 1. Use our full firm name of Jeselskis Brinkerhoff and Joseph, LLC2. Use our logo, attached AND our slogan - "THE NAME IS HARD TO REMEMBER. THE RESULTS ARE HARD TO FORGET." Please review the PDF attachments on the ad specs. The ad must follow the following requirements:• COLOR: Must be provided as CMYK, please convert if necessary. • IMAGES: All images must be precisely 300 dpi, placed at 100% to ensure print quality.• LOGOS: Preferred vector (.eps) format, (acceptable as high-res 300 dpi image).• TEXT: Should be editable within the ad. • PRIME COUNSEL REFERENCES: Please adhere to the attached advertising guidelines regarding the appropriate use of the Prime Counsel name, ad concepts and imagery.
Nice to have
• Highly stylized, memorable, upscale look. We really want to show our personality. We take our work seriously, but we don't take ourselves too seriously. Here are some other ads we like: https://issues.primecounsel.example/archive/ed1/page26 https://issues.primecounsel.example/archive/ed2/page4 https://www.searchlink.example/redirect?target=https%3A%2F%2Fwww.hollisvane.example%2Fhv-firm-honored-by-coastal-bar-review https://issues.primecounsel.example/archive/ed3/page4 https://issues.primecounsel.example/archive/ed4/page68
Should not have
• Scales of justice, traditional law firm style, or other design features that are predictable in law firm advertising. We don't like clutter or narrative copy.

```html
<!DOCTYPE html>
<html lang="en">
<head>
<meta charset="utf-8">
<title>Marwick Tolland and Pryce, LLC – Print Ad</title>
<link href="https://fonts.googleapis.com/css2?family=Cinzel:wght@400;500;600&family=Crimson+Pro:wght@600;700&family=Lato:ital,wght@0,400;0,700;1,400;1,700&display=swap" rel="stylesheet">
<style>
  :root{
    --backdrop:#b9dfe8;
    --navy:#121654;
    --navy-deep:#0c0f40;
    --sky:#1e8fd5;
    --name-blue:#3aa0e0;
    --yellow:#ffec00;
    --white:#ffffff;
    --rule:#2a5fa8;
    --ink:#1a1a2e;
  }
  *{box-sizing:border-box;margin:0;padding:0}
  html,body{width:1200px;height:2400px;overflow:hidden}
  body{background:var(--backdrop);position:relative;font-family:"Lato",sans-serif}
  .ad{position:absolute;left:50px;top:453px;width:1100px;height:1494px;background:var(--white);overflow:hidden}
  .ad__navy{position:absolute;left:0;top:0;width:1100px;height:1191px;background:linear-gradient(180deg,#141a5e 0%,var(--navy) 40%,var(--navy-deep) 100%)}
  .ad__title{position:absolute;left:0;top:70px;width:1100px;text-align:center;font-family:"Cinzel",serif;font-weight:500;font-size:64px;line-height:68px;color:var(--yellow);letter-spacing:1px}
  .tagline{position:absolute;left:0;top:230px;width:1100px;height:61px;background:var(--sky);display:flex;align-items:center;justify-content:center;font-family:"Crimson Pro",serif;font-weight:700;font-size:33px;color:var(--navy-deep)}
  .team-photo{position:absolute;left:408px;top:309px;width:620px;height:800px;background:radial-gradient(ellipse at 50% 45%,#5a6a8a 0%,#2f3d66 45%,rgba(18,22,84,0) 75%)}
  .honors{position:absolute;left:0;top:0;width:1100px;height:1191px}
  .honor{position:absolute;left:108px;width:440px;white-space:nowrap;color:var(--white);font-size:18px;line-height:21px}
  .honor__name{font-family:"Cinzel",serif;font-weight:400;font-size:21px;line-height:24px;color:var(--name-blue);margin-bottom:12px;letter-spacing:.5px}
  .honor__item{margin-bottom:8px}
  .honor__years{color:var(--yellow)}
  .honor__years--em{font-style:italic;font-weight:700}
  .honor__years--bold{font-weight:700}
  .rule{position:absolute;left:35px;height:1px;background:var(--rule)}
  .practice{position:absolute;left:61px;top:1125px;width:980px;height:112px;background:var(--yellow);display:flex;align-items:center}
  .practice__label{width:322px;padding-left:35px;font-family:"Cinzel",serif;font-size:21px;color:var(--ink);letter-spacing:1px;border-right:1px solid var(--ink);height:72px;display:flex;align-items:center}
  .practice__list{display:grid;grid-template-columns:350px 280px;row-gap:10px;padding-left:24px;font-size:15.5px;color:var(--ink)}
  .practice__list li{list-style:none;display:flex;align-items:center;gap:10px}
  .brand{position:absolute;left:94px;top:1272px;width:180px;height:180px;display:flex;align-items:center;justify-content:center}
  .brand__disc{position:absolute;inset:18px;border-radius:50%;background:var(--navy)}
  .brand__name{position:relative;font-family:"Cinzel",serif;font-weight:600;font-size:26px;color:var(--yellow);text-align:center;line-height:30px}
  .call{position:absolute;left:418px;top:1294px;width:626px;height:63px;display:flex}
  .call__label{width:323px;background:var(--sky);color:var(--navy-deep);font-size:38px;font-weight:400;display:flex;align-items:center;padding-left:24px;letter-spacing:.5px;white-space:nowrap}
  .call__number{flex:1;background:var(--yellow);color:var(--navy-deep);font-size:38px;display:flex;align-items:center;gap:12px;padding-left:6px;white-space:nowrap}
  .web{position:absolute;left:418px;top:1383px;display:flex;align-items:center;gap:14px;font-size:25px;color:var(--ink);white-space:nowrap}
  .divider{position:absolute;left:800px;top:1380px;width:2px;height:38px;background:var(--ink)}
  .social{position:absolute;left:868px;top:1388px;display:flex;gap:13px}
  .social span{width:30px;height:30px;border-radius:50%;background:var(--sky);display:block}
</style>
</head>
<body>
<main class="ad">
  <div class="ad__navy"></div>
  <h1 class="ad__title">MARWICK TOLLAND AND<br>PRYCE, LLC2</h1>
  <p class="tagline">The Name is Hard to Remember. The Results are Hard to Forget.</p>

  <div class="team-photo" role="img" aria-label="Group photo of the firm's four attorneys standing together"></div>

  <section class="honors">
    <div class="honor" style="top:357px">
      <h2 class="honor__name">RJ Tolland</h2>
      <p class="honor__item">Selected to Prime Counsel<br><span class="honor__years honor__years--em">2019 – 2022</span></p>
      <p class="honor__item">Selected to Emerging Leaders<br><span class="honor__years honor__years--em">2014, 2018</span></p>
    </div>
    <div class="rule" style="top:516px;width:370px"></div>
    <div class="honor" style="top:545px">
      <h2 class="honor__name">Helena Kerr Pryce</h2>
      <p class="honor__item">Selected to Prime Counsel<br><span class="honor__years">2018 – 2022</span></p>
      <p class="honor__item">Selected to Emerging Leaders<br><span class="honor__years">2013 – 2017</span></p>
    </div>
    <div class="rule" style="top:701px;width:400px"></div>
    <div class="honor" style="top:733px">
      <h2 class="honor__name">Katherine Marwick</h2>
      <p class="honor__item">Selected to Prime Counsel<br>Top 25 Women <span class="honor__years">2019, 2022</span></p>
      <p class="honor__item">Selected to Prime Counsel<br><span class="honor__years">2015 -2022</span></p>
      <p class="honor__item">Selected to Emerging Leaders<br><span class="honor__years">2011 – 2013</span></p>
    </div>
    <div class="rule" style="top:934px;width:420px"></div>
    <div class="honor" style="top:967px">
      <h2 class="honor__name">Adriana Whitcombe</h2>
      <p class="honor__item">Selected to Emerging Leaders<br><span class="honor__years honor__years--bold">2020 – 2022</span></p>
    </div>
  </section>

  <section class="practice">
    <div class="practice__label">OUR PRACTICE&nbsp; AREAS:</div>
    <ul class="practice__list">
      <li><svg width="15" height="15" viewBox="0 0 16 16"><circle cx="8" cy="8" r="8" fill="#1a1a2e"/><path d="M4.3 8.2l2.4 2.4 5-5" stroke="#ffec00" stroke-width="2" fill="none"/></svg>Business Litigation &amp; Dispute Resolution</li>
      <li><svg width="15" height="15" viewBox="0 0 16 16"><circle cx="8" cy="8" r="8" fill="#1a1a2e"/><path d="M4.3 8.2l2.4 2.4 5-5" stroke="#ffec00" stroke-width="2" fill="none"/></svg>Employment &amp; Labor</li>
      <li><svg width="15" height="15" viewBox="0 0 16 16"><circle cx="8" cy="8" r="8" fill="#1a1a2e"/><path d="M4.3 8.2l2.4 2.4 5-5" stroke="#ffec00" stroke-width="2" fill="none"/></svg>Entrepreneurship &amp; Small Business</li>
      <li><svg width="15" height="15" viewBox="0 0 16 16"><circle cx="8" cy="8" r="8" fill="#1a1a2e"/><path d="M4.3 8.2l2.4 2.4 5-5" stroke="#ffec00" stroke-width="2" fill="none"/></svg>Contract and Commercial Law</li>
    </ul>
  </section>

  <div class="brand">
    <div class="brand__disc"></div>
    <span class="brand__name">MTP<br>LEGAL</span>
  </div>

  <div class="call">
    <div class="call__label">CALL US NOW</div>
    <div class="call__number">
      <svg width="34" height="34" viewBox="0 0 34 34"><circle cx="17" cy="17" r="17" fill="#0c0f40"/><path d="M11 9.5l3.5-.5 2 4.5-2.2 1.5a11 11 0 0 0 5.2 5.2l1.5-2.2 4.5 2-.5 3.5c-.3 1-1.2 1.5-2.2 1.4C15.5 24.2 9.8 18.5 9.1 11.7 9 10.7 9.7 9.8 11 9.5z" fill="#ffec00"/></svg>
      317-555-0142
    </div>
  </div>

  <div class="web">
    <svg width="28" height="28" viewBox="0 0 28 28" fill="none" stroke="#1e8fd5" stroke-width="2"><circle cx="14" cy="14" r="12"/><ellipse cx="14" cy="14" rx="5" ry="12"/><path d="M2 14h24M4 8h20M4 20h20"/></svg>
    www.mtplawgroup.example
  </div>
  <div class="divider"></div>
  <div class="social" aria-label="Social media links"><span></span><span></span><span></span><span></span></div>
</main>
</body>
</html>
```